Modern Website For Law Firm Lawyer Melbourne, Australia Coded

We are looking for a modern and sophisticated website design. We would prefer the site to be based on WordPress given it is intuitive and some of our staff have experience using it.

Our law firm is based in Melbourne, Australia and we deal with property. The website must be hosted on a reliable Australian server.

We would also appreciate it if the designer can provide some guidance about how to make changes/upload content, such as photos and articles. We are happy to pay for this advice.

We prefer classic fonts in black or grey. We would also like a dash of colour so please use a green, blue or aqua colour palette that is consistent with our logo attached.

We do not want any law related images - scales of justice, gavel or the like.

Our ultimate goal is to communicate that the firm is professional, affordable, modern, dynamic, knowledgeable and one with the community.

We would like the following pages/sections/icons:

1. Who We Are - we will provide content.

2. Our Services - 1. Property 2. Wills, 3. Powers of Attorney 4. Probate & Estate Administration 5.Consultancy & Agency- we will provide content for each of these sections.

3. Articles - we already have approximately 20 articles on a wordpress blog and would like to port these articles to the website. We can do this ourselves if the designer can give us instructions about how to do this. We would also like to give clients the option to subscribe to our articles.

4. Contact Us - this should include our firms contact details; location map and we would like to give clients the option to "Request A Quote" directly from the page - i.e they will need to provide their full name, phone number email address, choose subject from drop down menu and type a message that gets sent to our outlook email.

5. Terms and Conditions - we will provide content

We really like the style and photographs used in the following website and want something as close to this as possible:

https://www.velbrook.com/

For privacy reasons, we would prefer to provide content together with all business details once we have decided on the winner.

We will monitor entries closely and promise to provide feedback and guidance on each entry.

This project is guaranteed. If our budget is too low please email us so we can discuss further and perhaps increase our budget. We are reasonable in this regard.

Thank you very much for considering this project.

Target Market(s)

General public, professionals, lawyers and conveyancers

Industry/Entity Type

Law Firm

Coding

Coded - Design and coding required

Number of Pages Required

1 page

Font styles to use
Sans Serif

Colors
33b8a4
33a6d7
0692cd
3176b5
00a990
9bcb3c
86cfc6
cadf82
85acd3

Requirements
Must have
• 1. Site must be coded and hosted on a reliable Australian server and it would be much appreciated if the deisgner provides instructions about how to add photos, blog articles etc-
• 2. The site must be secure and have green lock at top of page
• 3. Request A Quote - name, email, phone, drop down subject, message - email to our outlook email
• 4. Article Subscription
• 5. Domain (we have already purchased)
• 6. Location map
• 7. Facebook, LinkedIn, Instagram Icons
• 8. Membership icons in this order - KRT Member > Coastal Female Advocates > Guides From Counsel > Creature Foundation > Dorvo > Malpeth > Kel QR logos attached to go on bottom of page
• 9. Testimonials
Nice to have
• A modern, sophisticated website like:
• https://www.velbrook.com/ - we really like the style of the velbrook photographs
• We also really like this design by Tk of Sketch hive:
• https://www.sketchhive.com.au/design/58201346
Should not have
• Law related images - scales of justice gavel and the like

```html
<!DOCTYPE html>
<html lang="en">
<head>
<meta charset="utf-8">
<title>Larchmont Lawyers</title>
<link rel="stylesheet" href="https://fonts.googleapis.com/css2?family=Montserrat:wght@400;500;600&family=Lato:wght@400;700&display=swap">
<style>
:root{
  --teal:#2cb1c1;
  --teal-dark:#1f9fae;
  --blue:#0b63b4;
  --aqua:#33b8a4;
  --lime:#9bcb3c;
  --sky:#33a6d7;
  --ink:#333b40;
  --grey:#777;
  --panel:#ececec;
  --btn-dark:#2d3a40;
  --white:#fff;
}
*{box-sizing:border-box;margin:0;padding:0}
html,body{width:1200px;height:2620px;overflow:hidden;background:var(--white)}
body{position:relative;font-family:'Lato',sans-serif;color:var(--ink)}
.abs{position:absolute}
.topbar{left:0;top:0;width:1200px;height:49px;background:var(--teal);color:var(--white);font-size:12px;font-family:'Montserrat',sans-serif}
.topbar .contact{left:100px;top:17px;display:flex;gap:26px;letter-spacing:.3px}
.topbar .contact span{display:flex;align-items:center;gap:8px}
.social{display:flex;gap:10px}
.social span{width:24px;height:24px;border:1.5px solid var(--white);border-radius:50%;display:block}
.topbar .social{right:100px;top:12px}
.header{left:0;top:49px;width:1200px;height:101px;background:var(--white)}
.brand{left:100px;top:28px;display:flex;align-items:center;gap:12px;font-family:'Montserrat',sans-serif;color:var(--ink)}
.brand .mark{width:40px;height:40px;border-radius:50%;background:var(--sky)}
.brand b{display:block;font-size:22px;font-weight:500;line-height:1.05;letter-spacing:.5px}
.nav{left:382px;top:41px;display:flex;gap:34px;font-family:'Montserrat',sans-serif;font-size:13px;font-weight:500;color:var(--ink)}
.search{left:1075px;top:39px}
.stripe{left:0;width:1200px;height:5px;display:flex}
.stripe i{flex:1}
.stripe i:nth-child(1){background:var(--lime)}
.stripe i:nth-child(2){background:var(--sky)}
.stripe i:nth-child(3){background:var(--aqua)}
.stripe i:nth-child(4){background:var(--lime)}
.hero{left:0;top:154px;width:1200px;height:486px;background:linear-gradient(100deg,#2a4a72 0%,#3f79c4 35%,#4a86d2 60%,#3b74bf 100%)}
.hero-title{left:560px;top:70px;width:440px;text-align:center;color:var(--white);font-family:'Montserrat',sans-serif}
.hero-title h1{font-size:68px;font-weight:600;line-height:1.03;letter-spacing:1px}
.hero-title p{margin-top:18px;font-size:22px;letter-spacing:2px;font-weight:400}
.btn-outline{left:700px;top:278px;width:158px;height:40px;border:1.5px solid var(--white);color:var(--white);font-size:11px;font-family:'Montserrat',sans-serif;display:flex;align-items:center;justify-content:center}
.arrow{width:45px;height:44px;background:#1f2a33;display:flex;align-items:center;justify-content:center}
.dots{left:574px;top:432px;display:flex;gap:5px}
.dots i{width:11px;height:11px;border:1.5px solid var(--white)}
.dots i:first-child{background:var(--white)}
.hero-line{left:640px;top:437px;width:460px;height:1px;background:rgba(255,255,255,.8)}
.who{left:100px;top:611px;width:1002px;height:346px;background:var(--panel)}
.who h2{left:40px;top:58px;font-family:'Montserrat',sans-serif;font-size:24px;font-weight:400;color:var(--ink)}
.who p{left:40px;top:104px;width:450px;font-size:12px;line-height:21px;color:var(--grey);text-align:justify}
.btn-blue{background:var(--blue);color:var(--white);font-family:'Montserrat',sans-serif;font-size:12px;display:flex;align-items:center;justify-content:center}
.who .btn-blue{left:40px;top:241px;width:157px;height:46px}
.who .photo{left:522px;top:42px;width:437px;height:262px;border:5px solid #d7d7d7;background:linear-gradient(120deg,#6b4a32,#b99775 55,#d9c7b0)}
.accent-square{left:44px;top:959px;width:54px;height:53px;background:var(--teal)}
.section-head{left:0;width:1200px;text-align:center}
.section-head .dot{width:70px;height:70px;margin:0 auto;border-radius:50%;background:radial-gradient(circle,#fff 22%,var(--sky) 24%,var(--aqua) 60%,transparent 62%)}
.section-head h2{margin-top:28px;font-family:'Montserrat',sans-serif;font-size:24px;font-weight:400;color:var(--ink)}
.section-head hr{width:34px;border:0;border-top:2px solid var(--teal);margin:10px auto 0}
.services{left:0;top:1162px;width:1200px;height:293px;display:flex;border-top:1px solid #ddd;border-bottom:1px solid #ddd}
.service{flex:1;text-align:center;padding-top:34px}
.service:nth-child(even){background:#efefef}
.service svg{height:80px}
.service h3{margin-top:20px;font-family:'Montserrat',sans-serif;font-size:12px;font-weight:500;color:var(--ink)}
.service p{margin:10px auto 0;width:200px;font-size:10px;line-height:14px;color:var(--grey)}
.btn-dark{margin:14px auto 0;width:160px;height:30px;background:var(--btn-dark);color:var(--white);font-family:'Montserrat',sans-serif;font-size:10px;display:flex;align-items:center;justify-content:center}
.article{top:1670px;width:314px}
.article .photo{height:287px;position:relative}
.article .date{position:absolute;left:19px;bottom:16px;width:59px;height:58px;background:var(--teal);border:2px solid var(--white);color:var(--white);text-align:center;font-family:'Montserrat',sans-serif}
.article .date b{display:block;font-size:24px;font-weight:600;line-height:34px}
.article .date small{display:block;font-size:9px}
.article h3{margin:28px 0 0 16px;font-size:18px;font-weight:400;line-height:26px;color:var(--grey)}
.article .more{margin:8px 0 0 16px;font-family:'Montserrat',sans-serif;font-size:12px;font-weight:600;color:#1f3c5a;display:flex;align-items:center;gap:6px}
.view-all{left:520px;top:2096px;width:158px;height:48px}
.partners{left:90px;top:2192px;width:1020px;height:88px;display:flex;align-items:center;justify-content:space-between;font-family:'Montserrat',sans-serif;font-weight:600;font-size:26px;color:#3a2a6e}
.partners span{display:flex;align-items:center;gap:8px}
.partners i{width:16px;height:16px;background:#3a2a6e;display:block}
.partners .small{font-size:15px;width:130px;text-align:center;line-height:1.1}
.footer{left:0;top:2318px;width:1200px;height:302px;background:linear-gradient(180deg,#2aaebc,#2ab0b8);color:var(--white)}
.footer h4{font-family:'Montserrat',sans-serif;font-size:14px;font-weight:600}
.fcontact{left:98px;top:28px;font-size:12px}
.fcontact li{list-style:none;display:flex;gap:8px;margin-top:9px;line-height:15px}
.fcontact .social{margin-top:22px}
.map{left:375px;top:30px;width:345px;height:192px;background:linear-gradient(135deg,#e6e4d6,#d8e2c8 50%,#cfd9e4)}
.quote{left:795px;top:28px;width:305px}
.quote .fields{margin-top:10px;display:grid;grid-template-columns:148px 148px;gap:13px 9px}
.field{height:22px;background:rgba(255,255,255,.28);border:1px solid rgba(255,255,255,.5);font-size:11px;padding:4px 12px;display:flex;justify-content:space-between}
.field.msg{grid-column:1/3;height:56px}
.submit{margin-top:12px;width:127px;height:30px;border:1.5px solid var(--white);font-family:'Montserrat',sans-serif;font-size:11px;display:flex;align-items:center;justify-content:center}
.fline{left:98px;top:233px;width:1004px;height:1px;background:rgba(255,255,255,.6)}
.copy{left:0;top:260px;width:1200px;text-align:center;font-size:10px}
</style>
</head>
<body>

<div class="abs topbar">
  <div class="abs contact">
    <span><svg width="12" height="12" viewBox="0 0 12 12"><path d="M2 1l2 0 1 3-1.5 1a7 7 0 0 0 3.5 3.5L8 7l3 1v2a1 1 0 0 1-1 1A9 9 0 0 1 1 2a1 1 0 0 1 1-1z" fill="#fff"/></svg>CALL US: 123-456-7890</span>
    <span><svg width="13" height="10" viewBox="0 0 13 10"><rect x=".5" y=".5" width="12" height="9" fill="none" stroke="#fff"/><path d="M.5 .5l6 5 6-5" fill="none" stroke="#fff"/></svg>E-MAIL: INFO@EMAILADDRESS.COM</span>
  </div>
  <div class="abs social" aria-label="Social links"><span></span><span></span><span></span></div>
</div>

<header class="abs header">
  <div class="abs brand"><span class="mark"></span><div><b>LARCHMONT</b><b>LAWYERS</b></div></div>
  <nav class="abs nav"><span>WHO WE ARE</span><span>OUR SERVICES</span><span>ARTICLES</span><span>CONTACT US</span><span>TERMS AND CONDITIONS</span></nav>
  <svg class="abs search" width="20" height="20" viewBox="0 0 20 20"><circle cx="8" cy="8" r="6" fill="none" stroke="#999" stroke-width="1.6"/><path d="M12.5 12.5l5 5" stroke="#999" stroke-width="1.6"/></svg>
</header>
<div class="abs stripe" style="top:150px"><i></i><i></i><i></i><i></i></div>

<section class="abs hero" role="img" aria-label="Photo of a glass office tower against a blue sky with clouds">
  <div class="abs hero-title"><h1>LARCHMONT<br>LAWYERS</h1><p>ATTORNEYS &amp; ASSOCIATES</p></div>
  <div class="abs btn-outline">READ MORE</div>
  <div class="abs arrow" style="left:98px;top:197px"><svg width="18" height="14" viewBox="0 0 18 14"><path d="M17 7H2M7 1L1 7l6 6" fill="none" stroke="#fff" stroke-width="2"/></svg></div>
  <div class="abs arrow" style="left:1055px;top:197px"><svg width="18" height="14" viewBox="0 0 18 14"><path d="M1 7h15M11 1l6 6-6 6" fill="none" stroke="#fff" stroke-width="2"/></svg></div>
  <div class="abs dots"><i></i><i></i><i></i></div>
  <div class="abs hero-line"></div>
</section>

<section class="abs who">
  <h2 class="abs">WHO WE ARE</h2>
  <p class="abs">Lorem Ipsum is simply dummy text of the printing and typesetting industry. Lorem Ipsum has been the industry's standard dummy text ever since the 1500s, when an unknown printer took a galley of type and scrambled it to make a type specimen book. It has survived not only five centuries, but also the leap into electronic typesetting, remaining essentially unchanged.</p>
  <div class="abs btn-blue">READ MORE</div>
  <div class="abs photo" role="img" aria-label="Photo of two colleagues in conversation at a meeting table"></div>
</section>
<div class="abs accent-square"></div>

<div class="abs section-head" style="top:990px"><div class="dot"></div><h2>OUR SERVICES</h2><hr></div>

<section class="abs services">
  <div class="service">
    <svg viewBox="0 0 80 80"><circle cx="40" cy="40" r="37" fill="none" stroke="var(--aqua)" stroke-width="2.5"/><path d="M18 40L40 20l22 20M25 34v24h30V34" fill="none" stroke="var(--aqua)" stroke-width="2.5"/><rect x="35" y="44" width="10" height="14" fill="none" stroke="var(--aqua)" stroke-width="2.5"/></svg>
    <h3>PROPERTY LAW</h3><p>Lorem Ipsum is simply dummy text of the printing and typesetting industry. Lorem Ipsum has been the industry's standard dummy text ever since</p><div class="btn-dark">READ MORE</div>
  </div>
  <div class="service">
    <svg viewBox="0 0 80 80"><rect x="18" y="8" width="40" height="60" fill="none" stroke="var(--aqua)" stroke-width="2.5"/><path d="M26 22h24M26 32h24M26 42h16" stroke="var(--aqua)" stroke-width="2.5"/><path d="M48 62l16-22 4 3-16 22-6 2z" fill="none" stroke="var(--aqua)" stroke-width="2.5"/></svg>
    <h3>WILLS</h3><p>Lorem Ipsum is simply dummy text of the printing and typesetting industry. Lorem Ipsum has been the industry's standard dummy text ever since</p><div class="btn-dark">READ MORE</div>
  </div>
  <div class="service">
    <svg viewBox="0 0 80 80"><path d="M40 10v58M18 20h44M28 68h24" stroke="var(--aqua)" stroke-width="2.5"/><path d="M18 20l-8 20h16zM62 20l-8 20h16z" fill="none" stroke="var(--aqua)" stroke-width="2.5"/></svg>
    <h3>POWERS OF ATTORNEY</h3><p>Lorem Ipsum is simply dummy text of the printing and typesetting industry. Lorem Ipsum has been the industry's standard dummy text ever since</p><div class="btn-dark">READ MORE</div>
  </div>
  <div class="service">
    <svg viewBox="0 0 80 80"><path d="M12 34L40 10l28 24" fill="none" stroke="var(--aqua)" stroke-width="3"/><circle cx="40" cy="44" r="13" fill="var(--aqua)"/><text x="40" y="50" text-anchor="middle" font-family="Lato,sans-serif" font-size="17" fill="#fff">$</text><path d="M14 64h52M10 72h60" stroke="var(--aqua)" stroke-width="3"/></svg>
    <h3>PROBATE &amp; ESTATE ADMINISTRATION</h3><p>Lorem Ipsum is simply dummy text of the printing and typesetting industry. Lorem Ipsum has been the industry's standard dummy text ever since</p><div class="btn-dark">READ MORE</div>
  </div>
  <div class="service">
    <svg viewBox="0 0 80 80"><path d="M10 16h60v38H34l-12 12V54H10z" fill="none" stroke="var(--aqua)" stroke-width="2.5"/><path d="M20 28h40M20 38h40" stroke="var(--aqua)" stroke-width="2.5"/></svg>
    <h3>CONSULTANCY &amp; AGENCY</h3><p>Lorem Ipsum is simply dummy text of the printing and typesetting industry. Lorem Ipsum has been the industry's standard dummy text ever since</p><div class="btn-dark">READ MORE</div>
  </div>
</section>

<div class="abs section-head" style="top:1497px"><div class="dot"></div><h2>ARTICLES</h2><hr></div>

<div class="abs arrow" style="left:30px;top:1794px"><svg width="18" height="14" viewBox="0 0 18 14"><path d="M17 7H2M7 1L1 7l6 6" fill="none" stroke="#fff" stroke-width="2"/></svg></div>
<div class="abs arrow" style="left:1123px;top:1794px"><svg width="18" height="14" viewBox="0 0 18 14"><path d="M1 7h15M11 1l6 6-6 6" fill="none" stroke="#fff" stroke-width="2"/></svg></div>

<article class="abs article" style="left:100px">
  <div class="photo" role="img" aria-label="Photo of hands typing on a laptop beside a coffee cup" style="background:linear-gradient(135deg,#7a4a32,#c99a78 50%,#e8e2da)"><div class="date"><b>17</b><small>MARCH</small></div></div>
  <h3>Lorem Ipsum is simply dummy<br>text of the printing.</h3>
  <div class="more">READ MORE <svg width="12" height="12" viewBox="0 0 12 12"><circle cx="6" cy="6" r="5" fill="none" stroke="#1f3c5a" stroke-width="1.4"/><path d="M5 3.5L7.5 6 5 8.5" fill="none" stroke="#1f3c5a" stroke-width="1.4"/></svg></div>
</article>
<article class="abs article" style="left:442px">
  <div class="photo" role="img" aria-label="Photo of a hand holding a phone above a laptop keyboard" style="background:linear-gradient(135deg,#6a5a52,#b9aaa2 50%,#d8d4d2)"><div class="date"><b>20</b><small>APRIL</small></div></div>
  <h3>Lorem Ipsum is simply dummy<br>text of the printing.</h3>
  <div class="more">READ MORE <svg width="12" height="12" viewBox="0 0 12 12"><circle cx="6" cy="6" r="5" fill="none" stroke="#1f3c5a" stroke-width="1.4"/><path d="M5 3.5L7.5 6 5 8.5" fill="none" stroke="#1f3c5a" stroke-width="1.4"/></svg></div>
</article>
<article class="abs article" style="left:786px">
  <div class="photo" role="img" aria-label="Photo of a person writing notes next to a laptop" style="background:linear-gradient(135deg,#8fa3a6,#d7dcdc 50%,#4a5358)"><div class="date"><b>19</b><small>MAY</small></div></div>
  <h3>Lorem Ipsum is simply dummy<br>text of the printing.</h3>
  <div class="more">READ MORE <svg width="12" height="12" viewBox="0 0 12 12"><circle cx="6" cy="6" r="5" fill="none" stroke="#1f3c5a" stroke-width="1.4"/><path d="M5 3.5L7.5 6 5 8.5" fill="none" stroke="#1f3c5a" stroke-width="1.4"/></svg></div>
</article>

<div class="abs btn-blue view-all">VIEW ALL</div>

<section class="abs partners" aria-label="Memberships and partners">
  <span><i></i>Dorvo</span>
  <span>KRT</span>
  <span>Guides From Counsel</span>
  <span>Kel QR</span>
  <span>Malpeth</span>
  <span class="small">Coastal Female Advocates</span>
</section>

<footer class="abs footer">
  <div class="abs stripe" style="top:0"><i></i><i></i><i></i><i></i></div>
  <div class="abs fcontact">
    <h4>CONTACT US</h4>
    <ul>
      <li><svg width="10" height="14" viewBox="0 0 10 14"><path d="M5 13S1 8 1 5a4 4 0 0 1 8 0c0 3-4 8-4 8z" fill="#fff"/></svg>Lorem Ipsum is simply<br>Lorem Ipsum is simply dummy text</li>
      <li><svg width="12" height="12" viewBox="0 0 12 12"><path d="M2 1l2 0 1 3-1.5 1a7 7 0 0 0 3.5 3.5L8 7l3 1v2a1 1 0 0 1-1 1A9 9 0 0 1 1 2a1 1 0 0 1 1-1z" fill="#fff"/></svg>123.456.7890</li>
      <li><svg width="12" height="12" viewBox="0 0 12 12"><rect x="1" y="3" width="10" height="7" fill="#fff"/><rect x="3" y="1" width="6" height="3" fill="none" stroke="#fff"/></svg>123.456.7890</li>
      <li><svg width="13" height="10" viewBox="0 0 13 10"><rect x=".5" y=".5" width="12" height="9" fill="none" stroke="#fff"/><path d="M.5 .5l6 5 6-5" fill="none" stroke="#fff"/></svg>info@emailaddress.com</li>
    </ul>
    <div class="social" aria-label="Social links"><span></span><span></span><span></span></div>
  </div>
  <div class="abs map" role="img" aria-label="Location map showing the office"></div>
  <div class="abs quote">
    <h4>REQUEST A QUOTE</h4>
    <div class="fields">
      <div class="field">Full Name</div>
      <div class="field">Phone Number</div>
      <div class="field">Email Address</div>
      <div class="field">Choose Subject <span>&#8964;</span></div>
      <div class="field msg">Type a message</div>
    </div>
    <div class="submit">SUBMIT</div>
  </div>
  <div class="abs fline"></div>
  <div class="abs copy">Copyright © 2017 larchmont lawyers | Privacy Policy - Terms and Conditions</div>
</footer>

</body>
</html>
```